Christmas Flyer for a Newspaper Insert

Lumen Eyewear - Logo Attached

Lumen Eyewear is looking for a flyer design that will be inserted in a local newspaper and distributed to over 160,000 consumers. Lumen is an eyewear company that does designer prescription glasses, and designer sunwear. We have brands such as Brackwell, Sunvale, Colvi, Varn, Talmoni, Kelo Tam, etc.... The size should be 8.5 x 5.5. The end design will need to be printed twice on an 8.5 x 11 piece of paper and then cut in two.

Our offer is buy one get one at 50% off.
Restrictions are: not valid with some insurance plans

The look of Lumen is techy,somewhat industrial, and we use alot of silver, black and red. Our look is similar to Brackwell at Brackwell.com.
Updates

We will make a decision today on all designs and will need the high res art very fast.

Industry/Entity Type

Eyewear

Requirements
Must have
• Look at ads on Brackwell's website at Brackwell.com to get the look and feel.
Nice to have
• 5 Locations - Ash Court, Birch Plaza, Millstone, Fenwick, Harlow Ridge
• Website www.lumenvu.com

```html
<!DOCTYPE html>
<html lang="en">
<head>
<meta charset="utf-8">
<title>Lumen Eyewear – Buy One Get One Half Off</title>
<link href="https://fonts.googleapis.com/css2?family=Russo+One&family=Michroma&display=swap" rel="stylesheet">
<style>
  :root {
    --bg-deep: #050505;
    --bg-mid: #1d1d1f;
    --red: #e0121b;
    --red-dark: #7a0208;
    --red-glow: rgba(255, 30, 30, 0.55);
    --silver-hi: #ffffff;
    --silver-lo: #8d8f93;
    --text-light: #e8e8e8;
    --text-muted: #b5b5b5;
    --lens-dark: #2b2f2a;
    --lens-amber: #8a4a22;
  }
  * { margin: 0; padding: 0; box-sizing: border-box; }
  html, body { width: 1200px; height: 776px; overflow: hidden; background: var(--bg-deep); }
  .flyer {
    position: relative;
    width: 1200px;
    height: 776px;
    overflow: hidden;
    background:
      radial-gradient(ellipse 520px 260px at 50% 38%, rgba(120,120,125,0.35), transparent 70%),
      radial-gradient(ellipse 900px 500px at 50% 30%, var(--bg-mid), var(--bg-deep) 80%);
    font-family: "Michroma", sans-serif;
    color: var(--text-light);
    text-align: center;
  }
  .glow-streaks { position: absolute; inset: 0; }
  .product-shot {
    position: absolute;
    border-radius: 46% 46% 40% 40% / 60% 60% 40% 40%;
    filter: blur(1px);
  }
  .product-shot.top-left { left: 24px; top: 40px; width: 200px; height: 120px; transform: rotate(-8deg);
    background: radial-gradient(ellipse at 40% 50%, #5a6050, var(--lens-dark) 60%, #0c0c0c); }
  .product-shot.top-right { left: 980px; top: 96px; width: 200px; height: 106px; transform: rotate(6deg);
    background: radial-gradient(ellipse at 60% 50%, #5a6050, var(--lens-dark) 60%, #0c0c0c); }
  .product-shot.bottom-left { left: 30px; top: 360px; width: 220px; height: 120px; transform: rotate(-4deg);
    background: radial-gradient(ellipse at 45% 50%, #b0683a, var(--lens-amber) 55%, #1a0a05); }
  .product-shot.bottom-right { left: 940px; top: 388px; width: 240px; height: 106px; transform: rotate(4deg);
    background: radial-gradient(ellipse at 55% 50%, #b0683a, var(--lens-amber) 55%, #1a0a05); }

  .headline { position: absolute; left: 0; width: 100%; font-family: "Russo One", sans-serif; line-height: 1; text-transform: uppercase; white-space: nowrap; }
  .headline.red {
    color: var(--red);
    text-shadow:
      0 2px 0 #b30910, 0 4px 0 #960710, 0 6px 0 var(--red-dark),
      0 0 30px var(--red-glow);
  }
  .percent { top: 80px; font-size: 158px; letter-spacing: 2px; transform: scaleX(1.15); }
  .special-offer { top: 226px; font-size: 82px; letter-spacing: 2px; transform: scaleX(1.32); }
  .bogo {
    top: 310px; font-size: 82px; letter-spacing: 2px; transform: scaleX(1.1);
    background: linear-gradient(180deg, var(--silver-hi) 0%, #d9d9dc 45%, var(--silver-lo) 55%, #f3f3f3 100%);
    -webkit-background-clip: text; background-clip: text; color: transparent;
    filter: drop-shadow(0 4px 0 #3a3a3c) drop-shadow(0 0 18px rgba(255,255,255,0.25));
  }
  .half-off { top: 400px; font-size: 60px; letter-spacing: 3px; transform: scaleX(1.3); }

  .details { position: absolute; left: 0; width: 100%; top: 556px; font-size: 15px; letter-spacing: 1.5px; }
  .details p { margin-bottom: 9px; }
  .locations span + span::before { content: "|"; margin: 0 12px; color: var(--text-muted); }
  .website { font-size: 14px; }

  .brand { position: absolute; left: 0; width: 100%; top: 664px; }
  .brand-name { font-size: 32px; letter-spacing: 6px; color: var(--text-light); }
  .tagline { margin-top: 14px; font-size: 12px; letter-spacing: 17px; color: var(--text-muted); }
</style>
</head>
<body>
<main class="flyer">
  <svg class="glow-streaks" width="1200" height="776" viewBox="0 0 1200 776" aria-hidden="true">
    <defs>
      <linearGradient id="streak" x1="0" x2="1">
        <stop offset="0" stop-color="#ff2020" stop-opacity="0"/>
        <stop offset="0.5" stop-color="#ff3030" stop-opacity="0.9"/>
        <stop offset="1" stop-color="#ff2020" stop-opacity="0"/>
      </linearGradient>
      <radialGradient id="spark">
        <stop offset="0" stop-color="#fff" stop-opacity="0.9"/>
        <stop offset="1" stop-color="#fff" stop-opacity="0"/>
      </radialGradient>
    </defs>
    <rect x="160" y="180" width="880" height="4" fill="url(#streak)"/>
    <rect x="240" y="300" width="720" height="3" fill="url(#streak)"/>
    <rect x="120" y="392" width="960" height="3" fill="url(#streak)"/>
    <rect x="300" y="470" width="600" height="3" fill="url(#streak)"/>
    <g fill="url(#spark)">
      <circle cx="330" cy="120" r="4"/><circle cx="880" cy="150" r="3"/><circle cx="250" cy="300" r="3"/>
      <circle cx="960" cy="280" r="4"/><circle cx="420" cy="480" r="3"/><circle cx="800" cy="500" r="3"/>
      <circle cx="610" cy="40" r="3"/><circle cx="150" cy="250" r="2"/><circle cx="1050" cy="340" r="2"/>
      <circle cx="700" cy="490" r="2"/><circle cx="500" cy="60" r="2"/><circle cx="940" cy="60" r="2"/>
    </g>
  </svg>

  <div class="product-shot top-left" role="img" aria-label="Dark-lens sport sunglasses"></div>
  <div class="product-shot top-right" role="img" aria-label="Dark-lens wraparound sunglasses"></div>
  <div class="product-shot bottom-left" role="img" aria-label="Amber-lens tortoise sunglasses"></div>
  <div class="product-shot bottom-right" role="img" aria-label="Amber-lens tortoise sunglasses"></div>

  <h1 class="headline red percent">50%</h1>
  <p class="headline red special-offer">Special Offer</p>
  <p class="headline bogo">Buy One Get One</p>
  <p class="headline red half-off">Half Off</p>

  <section class="details">
    <p class="restrictions">Restrictions: Valid November 26th through 28th&nbsp; not valid with some insurance plans</p>
    <p class="locations"><span>Ash Court</span><span>Birch Plaza</span><span>Millstone</span><span>Fenwick</span><span>Harlow Ridge Website</span></p>
    <p class="website">www.lumenvu.com</p>
  </section>

  <footer class="brand">
    <div class="brand-name">LUMEN</div>
    <div class="tagline">VISION FOR EVERY VIEW</div>
  </footer>
</main>
</body>
</html>
```